Clean Air Information

I am uploading a rough draft on what I want. I am looking for different ideas on how to make it look more attractive and not so boring. I want it to really stand out and make a statement. Also, I am uploading additional documents for statement information or additional use.

Reason: I am providing more time to ensure there is enough time for all parties.

The most recent submissions are looking good. Please keep it coming, I have extended deadline.

```html
<!DOCTYPE html>
<html lang="en">
<head>
<meta charset="utf-8">
<title>Clear Haven – Cleaner Air Brochure</title>
<link rel="stylesheet" href="https://fonts.googleapis.com/css2?family=Arimo:ital,wght@0,400;0,700;1,400&display=swap">
<style>
  :root{
    --green:#3ea84a;
    --orange:#f26f22;
    --amber:#f7a81b;
    --ink:#111111;
    --white:#ffffff;
    --photo-light:#eef5fa;
    --photo-mid:#a9cfe8;
    --photo-deep:#6fa6cf;
  }
  *{box-sizing:border-box;margin:0;padding:0}
  html,body{width:1200px;height:927px;overflow:hidden;background:var(--white)}
  body{font-family:"Arimo",Arial,sans-serif;color:var(--ink)}
  .brochure{position:relative;width:1200px;height:927px;overflow:hidden;background:var(--white)}
  .backdrop{position:absolute;inset:0;width:1200px;height:927px}
  .fold{position:absolute;top:0;width:1px;height:927px;background:rgba(0,0,0,.08)}

  /* Inside panel */
  .panel-inside{position:absolute;left:48px;top:0;width:304px}
  .panel-inside__title{position:absolute;top:40px;left:-2px;width:300px;color:var(--white);font-size:23.5px;line-height:25px;font-weight:400}
  .panel-inside__body{position:absolute;top:124px;left:0;width:304px;font-size:13px;line-height:16.2px}
  .mold-photo{float:left;width:164px;height:164px;margin-left:-36px;margin-right:6px;margin-top:-4px;border-radius:50%;
    shape-outside:circle(50%);shape-margin:8px;
    background:radial-gradient(circle at 45% 40%,#b89a84,#96708a 55%,#7a5c7a);
    border:2px solid var(--white)}
  .section-title{color:var(--orange);font-weight:700;font-size:17.5px;line-height:20px}
  .section{margin-top:12px}
  .section p{margin-top:1px}
  .factor{color:var(--green);font-weight:700}
  .factor::before{content:"";display:inline-block;width:0;height:0;border-left:6px solid var(--green);border-top:4.5px solid transparent;border-bottom:4.5px solid transparent;margin-right:4px;vertical-align:1px}

  /* Middle panel */
  .panel-contact{position:absolute;left:398px;top:0;width:404px;text-align:center}
  .brand-mark{position:absolute;top:298px;left:0;width:404px;display:flex;align-items:center;justify-content:center;gap:12px}
  .brand-mark__dot{width:58px;height:58px;border-radius:50%;background:var(--green)}
  .brand-mark__name{font-size:28px;font-weight:700;color:var(--green)}
  .partner{position:absolute;top:492px;left:0;width:404px;display:flex;align-items:center;justify-content:center;gap:8px}
  .partner__square{width:18px;height:18px;background:var(--ink)}
  .partner__name{font-size:13px;font-weight:700}
  .contact{position:absolute;top:592px;left:0;width:404px;font-weight:700;font-style:normal}
  .contact__name{font-size:17.5px;line-height:22px}
  .contact__address{font-size:14px;line-height:20px;margin-top:6px}
  .contact__lines{font-size:14px;line-height:20px;margin-top:8px}

  /* Cover panel */
  .panel-cover{position:absolute;left:802px;top:0;width:398px;text-align:center}
  .cover-brand{position:absolute;top:56px;left:20px;width:360px;display:flex;align-items:center;justify-content:center;gap:12px}
  .cover-brand__dot{width:48px;height:48px;border-radius:50%;background:var(--green)}
  .cover-brand__name{font-size:32px;font-weight:700;color:var(--ink)}
  .tagline{position:absolute;top:126px;left:0;width:398px;color:var(--orange);font-style:italic;font-size:24px;line-height:25px}
  .headline{position:absolute;top:250px;left:0;width:398px;font-size:41px;line-height:40px;font-weight:400}
  .cover-contact{position:absolute;top:812px;left:0;width:398px;color:var(--white);font-size:28px;line-height:36px}
</style>
</head>
<body>
<main class="brochure">
  <svg class="backdrop" viewBox="0 0 1100 850" preserveAspectRatio="none" aria-hidden="true">
    <defs>
      <linearGradient id="photoFill" x1="0" y1="0" x2="0" y2="1">
        <stop offset="0" stop-color="var(--white)"/>
        <stop offset=".3" stop-color="var(--photo-light)"/>
        <stop offset=".65" stop-color="var(--photo-mid)"/>
        <stop offset="1" stop-color="var(--photo-deep)"/>
      </linearGradient>
    </defs>
    <rect x="735" y="190" width="365" height="540" fill="url(#photoFill)" role="img" aria-label="Photo of a calm mountain lake with forest and clouds"/>
    <path d="M0,0 H735 V115 C650,85 540,62 410,72 C280,82 190,100 145,118 C90,140 40,190 0,235 Z" fill="var(--green)"/>
    <path d="M145,118 C190,100 280,82 410,72 C540,62 650,85 735,115 L735,128 C650,98 540,78 410,86 C290,94 210,110 150,128 Z" fill="var(--amber)"/>
    <path d="M400,80 C540,70 650,92 735,120 L735,128 C650,98 540,78 410,86 Z" fill="var(--orange)"/>
    <path d="M0,730 C130,790 300,830 470,832 C600,833 690,800 735,745 V850 H0 Z" fill="var(--amber)"/>
    <path d="M0,740 C130,800 300,840 470,842 C600,843 690,808 735,755 V850 H0 Z" fill="var(--green)"/>
    <path d="M735,705 C840,665 990,645 1100,665 V850 H735 Z" fill="var(--orange)"/>
    <path d="M735,735 C850,700 990,690 1100,722 V850 H735 Z" fill="var(--green)"/>
  </svg>
  <div class="fold" style="left:398px"></div>
  <div class="fold" style="left:802px"></div>

  <section class="panel-inside">
    <h2 class="panel-inside__title">What you may not know about those dark corners</h2>
    <div class="panel-inside__body">
      <div class="mold-photo" role="img" aria-label="Close-up photo of colourful mold growth"></div>
      <h3 class="section-title">What is mold</h3>
      <p>Molds are classified as fungi and can be found nearly everywhere in the natural world. While they have an important job to play in nature by breaking down dead organic matter such as fallen leaves or dead trees, mold growth indoors can be destructive and dangerous.</p>
      <div class="section">
        <h3 class="section-title">Why it concerns you</h3>
        <p>The very same properties that make mold important in its natural environment can ultimately cause damage to the structure of your home, the internal systems that keep your home comfortable and functioning, and your personal possessions. More importantly, it can also seriously affect the health of everyone in your household, especially in those who have allergies, respiratory conditions such as asthma, and autoimmune disorders.</p>
      </div>
      <div class="section">
        <h3 class="section-title">Ideal Conditions</h3>
        <p>Mold requires four things to grow<br>and prosper:<br>
        <span class="factor">Spores.</span> These are found everywhere<br>in nature and can enter your house through vents, open windows, on pets, or even on your skin.<br>
        <span class="factor">Nutrients.</span> Mold can use almost any carbon-based organic material for nutrients; meaning anything from wood to pet dander to generic dust that general everyday activity can produce.<br>
        <span class="factor">Proper Temperature.</span> Unfortunately, mold prefers the same kind of temperatures we do: not too hot and not too cold, so our homes provide a great environment for mold to prosper.<br>
        <span class="factor">Moisture.</span> Areas with heavy humidity, leaks, or any kind of water damage are all potential breeding grounds for molds. Eliminating any one of these four factors can prohibit mold growth in your home.</p>
      </div>
    </div>
  </section>

  <section class="panel-contact">
    <div class="brand-mark"><span class="brand-mark__dot"></span><span class="brand-mark__name">CLEAR HAVEN</span></div>
    <div class="partner"><span class="partner__square"></span><span class="partner__name">R&amp;M Advisory</span></div>
    <address class="contact">
      <div class="contact__name">CLEAR HAVEN</div>
      <div class="contact__address">4120 Meadowbrook Dr<br>Suite 210<br>Garland Heights, TX 75000</div>
      <div class="contact__lines">Phone: 555-014-2387<br>Fax: 555-019-6620<br>www.rm-advisory.example</div>
    </address>
  </section>

  <section class="panel-cover">
    <div class="cover-brand"><span class="cover-brand__dot"></span><span class="cover-brand__name">CLEAR HAVEN</span></div>
    <p class="tagline">Cleaner air<br>...because we care</p>
    <h1 class="headline">Bring fresh air<br>into your home</h1>
    <p class="cover-contact">555-014-2387<br>www.rm-advisory.example</p>
  </section>
</main>
</body>
</html>
```